Kivora - a fintech company - business card

We need a business card design for our Payments Technology company in Sydney, Australia. We provide business with payment solutions expanding across EFTPOS machines, online payment gateways and mobile payment solutions. We would like to see designs that are clean, classy and professional.
Target Market(s)
Business professionals, executives, c-suite
Industry/Entity Type
Fintech
Contact Information for Business Card
Will be on 400gsm. Logo will most likely be spot gloss unless designer recommends otherwise.
Font styles to use
Sans Serif
Requirements
Must have
- We need our website (kivora.com.au), email (contact@kivora.com.au), mobile (0455 806 274) and direct phone number (02 7391 5082) to feature on the card along with our logo (attached) and the words "EFTPOS | ONLINE | MOBILE"
- Font = Roboto

```html
<!DOCTYPE html>
<html lang="en">
<head>
<meta charset="utf-8">
<title>Kivora – Business Card</title>
<link rel="stylesheet" href="https://fonts.googleapis.com/css2?family=Roboto:wght@400;500;700&display=swap">
<style>
  :root {
    --backdrop: #3a3a3a;
    --brand-blue: #15609a;
    --brand-blue-deep: #124f80;
    --card-white: #ffffff;
    --text-grey: #6b6b6d;
    --icon-blue: #1d5f96;
  }
  * { box-sizing: border-box; margin: 0; padding: 0; }
  html, body {
    width: 1200px;
    height: 900px;
    overflow: hidden;
  }
  body {
    background: var(--backdrop);
    font-family: "Roboto", sans-serif;
    display: flex;
    flex-direction: column;
    align-items: center;
    justify-content: center;
    gap: 40px;
  }
  .card {
    width: 600px;
    height: 367px;
    position: relative;
    overflow: hidden;
  }
  .card-back {
    background: var(--brand-blue);
    display: flex;
    align-items: center;
    justify-content: center;
  }
  .card-back .wordmark {
    font-weight: 700;
    font-size: 46px;
    letter-spacing: 3px;
    text-transform: uppercase;
    color: var(--brand-blue-deep);
  }
  .card-front {
    background: var(--card-white);
  }
  .brand-band {
    position: absolute;
    left: 0;
    top: 0;
    width: 270px;
    height: 100%;
    background: var(--brand-blue);
  }
  .contact-block {
    position: absolute;
    left: 318px;
    top: 138px;
  }
  .company-name {
    font-weight: 700;
    font-size: 36px;
    line-height: 1;
    letter-spacing: 1px;
    text-transform: uppercase;
    color: var(--text-grey);
  }
  .service-line {
    margin-top: 4px;
    font-weight: 500;
    font-size: 19px;
    letter-spacing: 1.2px;
    color: var(--brand-blue);
  }
  .service-line .divider { color: var(--text-grey); font-weight: 400; }
  .contact-list {
    list-style: none;
    margin-top: 10px;
  }
  .contact-item {
    display: flex;
    align-items: center;
    gap: 10px;
    font-size: 19px;
    font-weight: 400;
    color: var(--text-grey);
    letter-spacing: 0.6px;
    line-height: 29px;
  }
  .contact-icon {
    width: 17px;
    height: 17px;
    fill: var(--icon-blue);
    flex: none;
  }
</style>
</head>
<body>

  <section class="card card-back" aria-label="Business card back">
    <span class="wordmark">Kivora</span>
  </section>

  <section class="card card-front" aria-label="Business card front">
    <div class="brand-band"></div>

    <div class="contact-block">
      <h1 class="company-name">Kivora</h1>
      <p class="service-line">EFTPOS <span class="divider">|</span> ONLINE <span class="divider">|</span> MOBILE</p>

      <ul class="contact-list">
        <li class="contact-item">
          <svg class="contact-icon" viewBox="0 0 24 24" aria-hidden="true"><path d="M6.6 10.8a15.1 15.1 0 0 0 6.6 6.6l2.2-2.2a1 1 0 0 1 1-.25 11.4 11.4 0 0 0 3.6.57 1 1 0 0 1 1 1V20a1 1 0 0 1-1 1A17 17 0 0 1 3 4a1 1 0 0 1 1-1h3.5a1 1 0 0 1 1 1c0 1.25.2 2.45.57 3.6a1 1 0 0 1-.25 1z"/></svg>
          <span>02 7391 5082</span>
        </li>
        <li class="contact-item">
          <svg class="contact-icon" viewBox="0 0 24 24" aria-hidden="true"><path d="M7 1h10a2 2 0 0 1 2 2v18a2 2 0 0 1-2 2H7a2 2 0 0 1-2-2V3a2 2 0 0 1 2-2zm0 3v14h10V4zm5 15.5a1.2 1.2 0 1 0 0 2.4 1.2 1.2 0 0 0 0-2.4z"/></svg>
          <span>0455 806 274</span>
        </li>
        <li class="contact-item">
          <svg class="contact-icon" viewBox="0 0 24 24" aria-hidden="true"><path d="M2 5h20v1.2l-10 6.3L2 6.2zm0 3.5 10 6.2 10-6.2V19H2z"/></svg>
          <span>contact@kivora.com.au</span>
        </li>
        <li class="contact-item">
          <svg class="contact-icon" viewBox="0 0 24 24" aria-hidden="true"><path d="M12 2a10 10 0 1 0 0 20 10 10 0 0 0 0-20zm6.9 6h-2.9a15.7 15.7 0 0 0-1.4-3.6A8 8 0 0 1 18.9 8zM12 4c.8 1.2 1.5 2.5 1.9 4h-3.8c.4-1.5 1.1-2.8 1.9-4zM4.3 14a8 8 0 0 1 0-4h3.4a16 16 0 0 0 0 4zm.8 2h2.9a15.7 15.7 0 0 0 1.4 3.6A8 8 0 0 1 5.1 16zM8 8H5.1a8 8 0 0 1 4.3-3.6C8.8 5.5 8.3 6.7 8 8zm4 12c-.8-1.2-1.5-2.5-1.9-4h3.8c-.4 1.5-1.1 2.8-1.9 4zm2.3-6H9.7a14.6 14.6 0 0 1 0-4h4.6a14.6 14.6 0 0 1 0 4zm.3 5.6c.6-1.1 1.1-2.3 1.4-3.6h2.9a8 8 0 0 1-4.3 3.6zm1.7-5.6a16 16 0 0 0 0-4h3.4a8 8 0 0 1 0 4z"/></svg>
          <span>www.kivora.com.au</span>
        </li>
      </ul>
    </div>
  </section>

</body>
</html>
```